Marketing Flyer for Plumber Referals

8.5" x11" Layout should be landscape not portrait. Create a bold, eye-catching flyer that highlights earning potential from referrals for water damage restoration. Use high-contrast colors like blue, yellow, and white, with bold fonts and dynamic layouts. Include images of restoration work, cash, and happy clients. Emphasize key benefits like $500 minimum payouts, fast payments, and unlimited income potential. Keep instructions simple: refer a client, we handle the work, you get paid. Add a clear call-to-action and display contact details prominently. Focus on professionalism and energy.

Target Market(s)

Plumbers and Contractor 8.5" x11" Layout should be landscape not portrait.

Industry/Entity Type

General Contractor

Colors
0054AA
0677BA
7BADD7
CADEEF
E8F1F8
EB3D1F
EC4F4E
F09395
F8D3D4
FCEDEE

Requirements
Must have
• 8.5" x11" Layout should be landscape not portrait.
Nice to have

```html
<!DOCTYPE html>
<html lang="en">
<head>
<meta charset="utf-8">
<title>Harborline Builders – Referral Flyers</title>
<link href="https://fonts.googleapis.com/css2?family=Poppins:wght@400;600;700;800&family=Oswald:wght@500;600;700&display=swap" rel="stylesheet">
<style>
:root{
  --navy:#0b2470;
  --royal:#133a9e;
  --band:#0d2566;
  --sky:#4a88e8;
  --yellow:#eef20a;
  --red:#d42a12;
  --white:#ffffff;
  --ink:#1b1b1b;
  --stage:#e9e9e9;
}
*{margin:0;padding:0;box-sizing:border-box}
html,body{width:751px;height:1200px;overflow:hidden;background:var(--stage)}
body{position:relative;font-family:'Poppins',sans-serif}
.flyer{position:absolute;left:62px;width:627px;height:485px;background:var(--white);overflow:hidden}
.flyer--earn{top:80px}
.flyer--how{top:633px}
.abs{position:absolute}
.hero-bg{left:0;top:0;width:627px;background:linear-gradient(120deg,var(--navy) 0%,var(--royal) 60%,var(--navy) 100%)}
.brand{display:flex;flex-direction:column;align-items:center;justify-content:center;gap:6px;background:rgba(40,60,150,.45);color:var(--white);font-weight:400;letter-spacing:1px}
.brand-mark{width:10px;height:10px;border:1.5px solid var(--white);border-radius:50%}
.center-text{text-align:center;font-weight:800;line-height:1}
/* card 1 */
.earn{left:0;width:395px;top:97px;font-size:33px;color:var(--yellow)}
.unlimited{left:0;width:395px;top:125px;font-size:47px;color:var(--white);letter-spacing:-1px}
.cash{left:0;width:395px;top:170px;font-size:52px;color:var(--white)}
.refer-line{left:0;width:395px;top:225px;font-size:17px;color:var(--yellow);font-weight:700}
.pill{left:120px;top:256px;width:196px;height:45px;background:var(--red);border-radius:0 22px 22px 0;border:2px solid #a81c08}
.pill-text{left:150px;top:256px;height:45px;line-height:45px;font-family:'Oswald',sans-serif;font-weight:600;font-size:21px;color:var(--white)}
.minimum{left:73px;top:247px;width:60px;height:60px;border-radius:50%;background:var(--yellow);border:2px solid var(--white);text-align:center;color:var(--red)}
.minimum b{display:block;font-weight:800;font-size:19px;margin-top:11px;line-height:1}
.minimum b sup{font-size:9px}
.minimum span{display:block;font-family:'Oswald',sans-serif;font-size:10px;font-weight:500;line-height:1.2}
.or{left:130px;top:268px;width:18px;height:18px;border-radius:50%;background:#222;color:var(--white);font-size:8px;text-align:center;line-height:18px;border:1px solid var(--white)}
.badge{left:337px;top:180px;width:150px;height:150px}
.badge-text{left:337px;top:222px;width:150px;text-align:center;font-family:'Oswald',sans-serif;color:var(--white);line-height:1}
.badge-text .top{font-size:10px;font-weight:500}
.badge-text .num{font-size:46px;font-weight:700;color:var(--yellow);margin:1px 0}
.badge-text .bot{font-size:9px;font-weight:500;line-height:1.1}
.why{left:29px;top:307px;font-size:19px;font-weight:800;color:var(--sky)}
.perk{top:338px;width:150px;text-align:center}
.perk-icon{width:32px;height:32px;margin:0 auto 4px;border-radius:50%;background:var(--red);display:flex;align-items:center;justify-content:center}
.perk h3{font-size:9.5px;font-weight:700;color:var(--navy);line-height:1.2}
.perk p{font-size:6.5px;color:var(--ink);line-height:1.3}
.divider{top:372px;width:1px;height:34px;background:#444}
.tagband{left:0;top:410px;width:627px;height:26px;background:var(--band);color:var(--white);font-weight:700;font-size:13.5px;text-align:center;line-height:26px;word-spacing:2px}
.footer{left:0;width:627px;height:50px;background:var(--sky);color:var(--white)}
.footer .cta{position:absolute;left:29px;top:7px;font-weight:700;font-size:15px}
.footer .phone{position:absolute;left:283px;top:8px;font-weight:700;font-size:14.5px;display:flex;align-items:center;gap:5px}
.footer .web{position:absolute;left:427px;top:10px;font-weight:700;font-size:10.5px;display:flex;align-items:center;gap:5px}
/* card 2 */
.headline{left:0;width:390px;color:var(--white);font-size:41px;font-weight:800;text-align:center;line-height:1;letter-spacing:-.5px}
.howband{left:0;top:234px;width:627px;height:43px;background:var(--yellow)}
.how-title{left:0;top:234px;width:380px;height:43px;line-height:43px;text-align:center;font-weight:800;font-size:21px;color:var(--navy)}
.step{top:329px;width:161px;height:99px;border:1px solid #333;border-radius:8px;background:var(--white)}
.step-photo{top:297px;width:134px;height:81px;border:1px solid #333;border-radius:7px}
.step-text{top:389px;width:161px;text-align:center}
.step-text h3{font-size:7.5px;font-weight:700;color:var(--navy);line-height:1.1}
.step-text p{font-size:6px;color:var(--ink);line-height:1.2}
</style>
</head>
<body>

<!-- Flyer one: earn unlimited cash -->
<section class="flyer flyer--earn">
  <div class="abs hero-bg" style="height:282px"></div>
  <svg class="abs" style="left:0;top:0" width="627" height="300" viewBox="0 0 627 300">
    <defs>
      <linearGradient id="floodTones" x1="0" y1="0" x2="0" y2="1">
        <stop offset="0" stop-color="#c9c7c1"/>
        <stop offset=".55" stop-color="#a89a86"/>
        <stop offset="1" stop-color="#6f6f72"/>
      </linearGradient>
    </defs>
    <path d="M388,0 L627,0 L627,282 L530,310 Q505,318 488,300 L340,150 Q326,132 338,112 Q360,40 388,0 Z" fill="var(--sky)"/>
    <path role="img" aria-label="Photo of a flooded home interior with a staircase" d="M398,0 L627,0 L627,268 L528,296 Q508,302 494,290 L350,147 Q338,132 348,116 Q370,44 398,0 Z" fill="url(#floodTones)"/>
  </svg>

  <div class="abs brand" style="left:138px;top:6px;width:120px;height:89px;font-size:10.5px">
    <span class="brand-mark"></span>HARBORLINE BUILDERS
  </div>

  <div class="abs center-text earn">EARN</div>
  <div class="abs center-text unlimited">UNLIMITED</div>
  <div class="abs center-text cash">CA$H</div>
  <div class="abs center-text refer-line">GET PAID TO REFER A FLOOD</div>

  <div class="abs pill"></div>
  <div class="abs pill-text">10% PER REFERRAL!</div>
  <div class="abs minimum"><b><sup>$</sup>500</b><span>MINIMUM</span></div>
  <div class="abs or">OR</div>

  <svg class="abs badge" viewBox="0 0 150 150" aria-hidden="true">
    <g fill="var(--red)">
      <rect x="24" y="24" width="102" height="102"/><rect x="24" y="24" width="102" height="102" transform="rotate(15 75 75)"/><rect x="24" y="24" width="102" height="102" transform="rotate(30 75 75)"/><rect x="24" y="24" width="102" height="102" transform="rotate(45 75 75)"/><rect x="24" y="24" width="102" height="102" transform="rotate(60 75 75)"/><rect x="24" y="24" width="102" height="102" transform="rotate(75 75 75)"/>
    </g>
    <g fill="var(--yellow)">
      <rect x="30" y="30" width="90" height="90"/><rect x="30" y="30" width="90" height="90" transform="rotate(15 75 75)"/><rect x="30" y="30" width="90" height="90" transform="rotate(30 75 75)"/><rect x="30" y="30" width="90" height="90" transform="rotate(45 75 75)"/><rect x="30" y="30" width="90" height="90" transform="rotate(60 75 75)"/><rect x="30" y="30" width="90" height="90" transform="rotate(75 75 75)"/>
    </g>
    <g fill="var(--red)">
      <rect x="32" y="32" width="86" height="86"/><rect x="32" y="32" width="86" height="86" transform="rotate(15 75 75)"/><rect x="32" y="32" width="86" height="86" transform="rotate(30 75 75)"/><rect x="32" y="32" width="86" height="86" transform="rotate(45 75 75)"/><rect x="32" y="32" width="86" height="86" transform="rotate(60 75 75)"/><rect x="32" y="32" width="86" height="86" transform="rotate(75 75 75)"/>
    </g>
  </svg>
  <div class="abs badge-text">
    <div class="top">PARTNER WITH THE</div>
    <div class="num">#1</div>
    <div class="bot">WATER DAMAGE<br>RESTORATION TEAM</div>
  </div>

  <div class="abs why">WHY PARTNER WITH US?</div>

  <div class="abs perk" style="left:8px">
    <div class="perk-icon"><svg width="16" height="16" viewBox="0 0 16 16"><circle cx="8" cy="8" r="6.5" fill="none" stroke="#fff" stroke-width="1.3"/><text x="8" y="11.5" text-anchor="middle" fill="#fff" font-size="10" font-weight="700" font-family="Poppins,sans-serif">$</text></svg></div>
    <h3>GUARANTEED PAYOUT</h3>
    <p>Minimum $500 or 10%<br>of the invoice, paid fast.</p>
  </div>
  <div class="abs divider" style="left:158px"></div>
  <div class="abs perk" style="left:157px">
    <div class="perk-icon"><svg width="16" height="16" viewBox="0 0 16 16"><rect x="3" y="2" width="10" height="12" rx="1" fill="none" stroke="#fff" stroke-width="1.3"/><path d="M5.5 8.5l2 2 3-4" fill="none" stroke="#fff" stroke-width="1.3"/></svg></div>
    <h3>FREE EVALUATIONS</h3>
    <p>We assess damage and process<br>insurance claims for your clients.</p>
  </div>
  <div class="abs divider" style="left:319px"></div>
  <div class="abs perk" style="left:313px">
    <div class="perk-icon"><svg width="16" height="16" viewBox="0 0 16 16"><circle cx="8" cy="5" r="2.6" fill="none" stroke="#fff" stroke-width="1.3"/><path d="M3 14c0-3 2.2-5 5-5s5 2 5 5" fill="none" stroke="#fff" stroke-width="1.3"/></svg></div>
    <h3>INDUSTRY LEADERS</h3>
    <p>Certified experts with<br>24/7 rapid response.</p>
  </div>
  <div class="abs divider" style="left:458px"></div>
  <div class="abs perk" style="left:459px">
    <div class="perk-icon"><svg width="16" height="16" viewBox="0 0 16 16"><path d="M8 2v12M2 8h12" stroke="#fff" stroke-width="1.3"/><circle cx="8" cy="2.5" r="1.5" fill="#fff"/><circle cx="2.5" cy="8" r="1.5" fill="#fff"/><circle cx="13.5" cy="8" r="1.5" fill="#fff"/></svg></div>
    <h3>AFFORDABLE SOLUTIONS</h3>
    <p>Lowest out-of-pocket<br>costs for your customers.</p>
  </div>

  <div class="abs tagband">SEND REFERRALS&nbsp; GET PAID GROW&nbsp; YOUR BUSINESS</div>

  <div class="abs footer" style="top:436px">
    <div class="cta">CALL TEXT OR BOOK ON-LINE</div>
    <div class="phone"><svg width="13" height="13" viewBox="0 0 16 16"><path d="M4 1.5l2.5 3-1.5 2c1 2 2.5 3.5 4.5 4.5l2-1.5 3 2.5-1.5 2.5C7 14 2 9 1.5 3z" fill="none" stroke="#fff" stroke-width="1.3"/></svg>555-014-2290</div>
    <div class="web"><svg width="11" height="11" viewBox="0 0 16 16"><circle cx="8" cy="8" r="6.5" fill="none" stroke="#fff" stroke-width="1.2"/><ellipse cx="8" cy="8" rx="3" ry="6.5" fill="none" stroke="#fff" stroke-width="1.2"/><path d="M1.5 8h13" stroke="#fff" stroke-width="1.2"/></svg>www.HarborlineRestore.com</div>
  </div>
</section>

<!-- Flyer two: how it works -->
<section class="flyer flyer--how">
  <div class="abs hero-bg" role="img" aria-label="Night city skyline in deep blue tones" style="height:234px;background:linear-gradient(180deg,var(--navy) 0%,var(--royal) 55%,#0a1f5a 100%)"></div>
  <div class="abs howband"></div>
  <svg class="abs" style="left:0;top:0" width="627" height="300" viewBox="0 0 627 300">
    <defs>
      <linearGradient id="moneyTones" x1="0" y1="0" x2="1" y2="1">
        <stop offset="0" stop-color="#dcdcd6"/>
        <stop offset=".5" stop-color="#a7b3a6"/>
        <stop offset="1" stop-color="#8c9488"/>
      </linearGradient>
    </defs>
    <path d="M318,0 L627,0 L627,246 L480,288 Q455,294 438,278 L305,140 Q285,112 293,70 Q300,25 318,0 Z" fill="var(--sky)"/>
    <path role="img" aria-label="Photo of hundred-dollar bills with letter tiles spelling cash flow" d="M326,0 L627,0 L627,236 L478,276 Q458,281 444,267 L313,134 Q297,110 304,72 Q311,28 326,0 Z" fill="url(#moneyTones)"/>
  </svg>

  <div class="abs brand" style="left:110px;top:10px;width:158px;height:108px;font-size:13px">
    <span class="brand-mark"></span>HARBORLINE BUILDERS
  </div>

  <div class="abs headline" style="top:132px">GET PAID TO</div>
  <div class="abs headline" style="top:176px">REFER A FLOOD</div>

  <div class="abs how-title">HOW IT WORKS</div>

  <div class="abs step" style="left:48px"></div>
  <div class="abs step-photo" role="img" aria-label="Photo of a leaking white drain pipe" style="left:61px;background:linear-gradient(135deg,#e8e8e8,#9a9a9a)"></div>
  <div class="abs step-text" style="left:48px"><h3>REFER FLOOD, WATER AND<br>MOLD DAMAGE</h3><p>Call, book online, or text<br>us directly.</p></div>

  <div class="abs step" style="left:234px"></div>
  <div class="abs step-photo" role="img" aria-label="Affiliate marketing illustration showing join, promote and earn steps" style="left:247px;background:linear-gradient(90deg,#f2f2f2,#c9d2d6)"></div>
  <div class="abs step-text" style="left:234px"><h3>WE TAKE CARE OF<br>EVERYTHING</h3><p>Free evaluations,<br>insurance claims, and<br>professional service.</p></div>

  <div class="abs step" style="left:420px"></div>
  <div class="abs step-photo" role="img" aria-label="Yellow road sign reading get paid to share against a blue sky" style="left:433px;background:linear-gradient(135deg,#5f93d6,#cfe0f3 60%,#e8e23a)"></div>
  <div class="abs step-text" style="left:420px"><h3>GET PAID FAST</h3><p>$500 minimum or 10% of the<br>invoice within 48 hours<br>of final payment.</p></div>

  <div class="abs footer" style="top:435px">
    <div class="cta">CALL TEXT OR BOOK ON-LINE</div>
    <div class="phone"><svg width="13" height="13" viewBox="0 0 16 16"><path d="M4 1.5l2.5 3-1.5 2c1 2 2.5 3.5 4.5 4.5l2-1.5 3 2.5-1.5 2.5C7 14 2 9 1.5 3z" fill="none" stroke="#fff" stroke-width="1.3"/></svg>555-014-2290</div>
    <div class="web"><svg width="11" height="11" viewBox="0 0 16 16"><circle cx="8" cy="8" r="6.5" fill="none" stroke="#fff" stroke-width="1.2"/><ellipse cx="8" cy="8" rx="3" ry="6.5" fill="none" stroke="#fff" stroke-width="1.2"/><path d="M1.5 8h13" stroke="#fff" stroke-width="1.2"/></svg>www.HarborlineRestore.com</div>
  </div>
</section>

</body>
</html>
```